Business Card Design Project

- makeup artist business card

- original and creative

- Elegant design

- Feel free to come out with cool designs but stick to being elegant and attractive

- Design relates to makeup

- includes name, occupation, contact numbers, email, website

- regular size business card

- round corner card

- double sided

- on 1 side it should just have the website name in the center " browsandblush.example "

Industry/Entity Type

Business

Requirements
Must have
• Marla Voss
Makeup Artist
USA: +1 (415)872-6410
Singapore: +65 83027715
marlavoss@browsandblush.example
www.browsandblush.example
Should not have
• nothing cartoon looking.
Pictures of makeup being grab from the internet.. Examples: eyes or lips.

```html
<!DOCTYPE html>
<html lang="en">
<head>
<meta charset="utf-8">
<title>Marla Voss — Makeup Artist Business Card</title>
<link href="https://fonts.googleapis.com/css2?family=Open+Sans:ital,wght@0,400;0,700;1,400&display=swap" rel="stylesheet">
<style>
  :root {
    --backdrop: #141414;
    --card: #1d1d1d;
    --card-edge: #2a2a2a;
    --pink: #d63a8e;
    --pink-soft: #b5397a;
    --white: #f4f4f4;
    --photo-dark: #2a2727;
    --photo-mid: #6a6462;
    --photo-pink: #c8467f;
  }
  html, body {
    margin: 0;
    padding: 0;
    width: 1200px;
    height: 691px;
    overflow: hidden;
    background: var(--backdrop);
    font-family: "Open Sans", sans-serif;
  }
  .canvas {
    position: relative;
    width: 1200px;
    height: 691px;
    background: radial-gradient(ellipse at 50% 40%, #202020 0%, var(--backdrop) 75%);
  }
  .card {
    position: absolute;
    top: 17px;
    height: 660px;
    background: linear-gradient(160deg, #222 0%, var(--card) 45%, #181818 100%);
    box-shadow: 0 0 0 1px var(--card-edge), 0 6px 18px rgba(0,0,0,.6);
    overflow: hidden;
  }
  .card--contact { left: 31px; width: 374px; }
  .card--website { left: 422px; width: 374px; }
  .card--portrait { left: 813px; width: 379px; }

  .contact {
    position: absolute;
    left: 14px;
    bottom: 22px;
    color: var(--white);
  }
  .contact__name {
    margin: 0;
    font-size: 24px;
    font-weight: 700;
    line-height: 1.1;
  }
  .contact__name .surname { color: var(--pink); font-weight: 400; }
  .contact__role {
    margin: 1px 0 6px;
    font-size: 18px;
    font-style: italic;
  }
  .contact__line {
    margin: 0;
    font-size: 17px;
    line-height: 22px;
  }
  .contact__email { margin: 6px 0 0; font-size: 17px; }
  .contact__web {
    margin: 12px 0 0;
    font-size: 20px;
    font-weight: 700;
    color: var(--pink);
  }

  .website {
    position: absolute;
    left: 196px;
    top: 178px;
    margin: 0;
    writing-mode: vertical-rl;
    font-size: 24px;
    color: var(--pink);
    letter-spacing: .5px;
    white-space: nowrap;
  }
  .website--reflection {
    left: 150px;
    transform: scaleX(-1);
    color: var(--pink-soft);
    opacity: .35;
    -webkit-mask-image: linear-gradient(to left, rgba(0,0,0,.9), rgba(0,0,0,.1));
            mask-image: linear-gradient(to left, rgba(0,0,0,.9), rgba(0,0,0,.1));
  }

  .portrait-photo {
    position: absolute;
    inset: 0;
    background:
      radial-gradient(ellipse 42% 30% at 35% 48%, var(--photo-pink) 0%, rgba(200,70,127,.4) 55%, transparent 80%),
      linear-gradient(170deg, var(--photo-dark) 0%, var(--photo-mid) 45%, #4a4544 75%, #1e1c1c 100%);
  }
  .portrait-caption {
    position: absolute;
    left: 22px;
    bottom: 18px;
    color: var(--white);
  }
  .portrait-caption__name {
    margin: 0;
    font-size: 27px;
    font-weight: 700;
  }
  .portrait-caption__name .surname { color: var(--pink); font-weight: 400; }
  .portrait-caption__title {
    margin: 0;
    font-size: 22px;
    font-weight: 400;
    line-height: 1.2;
  }
</style>
</head>
<body>
<main class="canvas">
  <section class="card card--contact">
    <div class="contact">
      <h1 class="contact__name">Marla <span class="surname">Voss</span></h1>
      <p class="contact__role">Makeup Artist</p>
      <p class="contact__line">USA: +1 (415)872-6410</p>
      <p class="contact__line">Singapore: +65 83027715</p>
      <p class="contact__email">marlavoss@browsandblush.example</p>
      <p class="contact__web">www.browsandblush.example</p>
    </div>
  </section>

  <section class="card card--website">
    <p class="website website--reflection" aria-hidden="true">www.browsandblush.example</p>
    <p class="website">www.browsandblush.example</p>
  </section>

  <section class="card card--portrait">
    <div class="portrait-photo" role="img" aria-label="Close-up beauty photograph of bright pink lips with fingertips and pale nails, in muted grey tones"></div>
    <div class="portrait-caption">
      <p class="portrait-caption__name">Marla <span class="surname">Voss</span></p>
      <p class="portrait-caption__title">Makeup Artist</p>
    </div>
  </section>
</main>
</body>
</html>
```